Design a landing page

We have a logo, we have colours in mind. What we need is to create a typical one-page landing page that would look nicely on both PC and mobile devices/tablets.

Typical layout - logo top left, top right - shop/client area buttons (links will open to different websites), informational area in the middle - image on the left + text on the right then image on the right + text on the left etc., then text links at the bottom (T&S, Cookie policy, privacy policy etc.).

Page must have cookie notification as per EU law.

We will also need help in preparing photos/images (up to 8) for the website.

End result should be either a Wordpress theme (preferred - so we can install it from wordpress control panel) or HTML/CSS page source. All scripts/images/files should be included - no external links to js/image libraries please.

The photo of the device attached. Primary users will be home users with placement on the ceiling, Minority of users will be business/commercial users with wall placements. Device is meant to monitor climat in the premises (Temperature, humidity, dew point) and alert users if readings are not within allowed range.

Need extra days to review

Industry/Entity Type

Microclimate Monitoring in premises

Coding

Coded - Design and coding required

Number of Pages Required

1 page

Colors
0054AA
0677BA
7BADD7
CADEEF
E8F1F8
0094D4
00A9DD
6FCCEA
C7EBF8
E9F6FB

Requirements
Must have
• White background, layout as described unless better option offered and accepted. Must have cookie warning.

```html
<!DOCTYPE html>
<html lang="en">
<head>
<meta charset="utf-8">
<title>Quadrell — Precision You Can Feel</title>
<link rel="stylesheet" href="https://fonts.googleapis.com/css2?family=Plus+Jakarta+Sans:wght@400;500;600;700;800&family=JetBrains+Mono:wght@500&display=swap">
<style>
:root{
  --navy:#13294b;
  --ink:#111418;
  --text:#3a4150;
  --muted:#6b7280;
  --teal:#4cc3c6;
  --pale:#f7f9fb;
  --white:#ffffff;
  --line:#e6e9ee;
}
*{box-sizing:border-box;margin:0;padding:0}
html,body{width:1200px;height:2566px;overflow:hidden}
body{font-family:"Plus Jakarta Sans",sans-serif;color:var(--ink);background:var(--white);position:relative}
.site-header{position:absolute;left:0;top:0;width:1200px;height:42px;background:var(--white);border-bottom:1px solid var(--line)}
.brand{position:absolute;left:218px;top:12px;font-weight:800;font-size:12px;color:var(--navy);letter-spacing:.3px}
.btn{display:inline-flex;align-items:center;justify-content:center;font-weight:600;font-size:9px;border-radius:4px;text-decoration:none;position:absolute}
.btn-outline{border:1.5px solid var(--navy);color:var(--navy);background:var(--white)}
.btn-solid{background:var(--navy);color:var(--white)}
.hero{position:absolute;left:0;top:42px;width:1200px;height:623px;overflow:hidden}
.hero-photo{position:absolute;inset:0;background:linear-gradient(100deg,#9a9894 0%,#6c6a6a 45%,#4a4f5a 100%)}
.eyebrow{font-family:"JetBrains Mono",monospace;font-size:7px;letter-spacing:1.4px;color:var(--teal);display:flex;align-items:center;gap:8px;position:absolute}
.eyebrow::before{content:"";width:19px;height:1px;background:var(--teal)}
.title{font-weight:800;letter-spacing:-1.5px;line-height:1.02;position:absolute}
.hero .title{left:617px;top:230px;font-size:45px;color:var(--white)}
.lead{font-size:11px;line-height:1.55;position:absolute}
.hero .lead{left:617px;top:333px;width:380px;color:var(--white);font-size:11.2px}
.stat{position:absolute;top:410px;height:49px;background:rgba(255,255,255,.82);border-radius:3px;padding:8px 10px}
.stat b{display:block;font-size:18px;font-weight:700;color:var(--navy);line-height:1}
.stat span{display:block;font-size:6.5px;color:var(--muted);letter-spacing:.4px;margin-top:5px}
.band{position:absolute;left:0;width:1200px}
.band-pale{background:var(--pale)}
.photo{position:absolute;width:420px;height:420px;border-radius:4px;box-shadow:0 14px 30px rgba(20,30,50,.12)}
.bracket{position:absolute;width:63px;height:64px;border-top:1.5px solid var(--teal);border-right:1.5px solid var(--teal)}
.feature .title{font-size:30px;letter-spacing:-1px}
.feature .lead{width:425px;color:var(--text);font-size:9.6px}
.chip{position:absolute;height:46px;background:var(--white);border-radius:3px;box-shadow:0 2px 8px rgba(20,30,50,.1);padding:7px 10px}
.chip b{display:block;font-size:18px;font-weight:700;color:var(--navy);line-height:1}
.chip span{display:block;font-size:6.5px;color:var(--muted);letter-spacing:.4px;margin-top:5px}
.site-footer{position:absolute;left:0;top:2460px;width:1200px;height:106px;background:var(--navy)}
.footer-links{position:absolute;left:441px;top:55px;display:flex;gap:25px}
.footer-links a{color:#e4e8ef;font-size:8.5px;text-decoration:none}
.copyright{position:absolute;left:444px;top:92px;font-family:"JetBrains Mono",monospace;font-size:6.5px;color:#7f8ca3}
.cookie{position:absolute;left:933px;top:2457px;width:251px;height:100px;background:var(--white);border-radius:6px;box-shadow:0 6px 20px rgba(0,0,0,.18);padding:14px 16px}
.cookie p{font-size:8px;line-height:1.6;color:var(--muted);width:205px}
.cookie strong{color:var(--navy);font-weight:700}
.cookie .btn{left:16px;top:64px;width:219px;height:21px;font-size:8px}
</style>
</head>
<body>

<header class="site-header">
  <div class="brand">QUADRELL</div>
  <a class="btn btn-outline" href="#" style="left:824px;top:7px;width:76px;height:27px">Client Hub</a>
  <a class="btn btn-solid" href="#" style="left:908px;top:7px;width:88px;height:27px">Secure Order</a>
</header>

<section class="hero">
  <div class="hero-photo" role="img" aria-label="Climate sensor mounted on a wall inside a warehouse"></div>
  <div class="eyebrow" style="left:617px;top:205px">NEXT-GEN MICROCLIMATE CONTROL</div>
  <h1 class="title">Precision You Can<br>Feel.</h1>
  <p class="lead">Deploy industrial-grade environmental monitoring across your professional or residential footprint. Real-time data processing for temperature, humidity, and dew point.</p>
  <div class="stat" style="left:617px;width:69px"><b>0.1°C</b><span>RESOLUTION</span></div>
  <div class="stat" style="left:706px;width:71px"><b>±2%</b><span>RH VARIANCE</span></div>
  <div class="stat" style="left:796px;width:61px"><b>24/7</b><span>UPTIME</span></div>
  <a class="btn btn-solid" href="#" style="left:617px;top:490px;width:122px;height:31px;font-size:9.5px">Initialize Setup</a>
</section>

<section class="band band-pale feature" style="top:665px;height:572px;border-bottom:1px solid var(--line)">
  <div class="bracket" style="left:522px;top:58px"></div>
  <div class="photo" style="left:153px;top:72px;background:linear-gradient(160deg,#c4c5c1,#9c9d98)" role="img" aria-label="Sensor mounted on a home ceiling"></div>
  <div class="eyebrow" style="left:636px;top:204px">ELEGANT INTEGRATION</div>
  <h2 class="title" style="left:636px;top:227px">Seamlessly Blends Into Your<br>Space.</h2>
  <p class="lead" style="left:636px;top:307px">AeroVera is engineered with a minimalist aesthetic to maintain the visual integrity of any environment. Optimized for wall-mount or ceiling-suspension configurations.</p>
  <a class="btn btn-outline" href="#" style="left:636px;top:338px;width:140px;height:26px;font-size:8.5px">Technical Documentation</a>
</section>

<section class="band feature" style="top:1237px;height:648px">
  <div class="bracket" style="left:1005px;top:62px"></div>
  <div class="photo" style="left:636px;top:75px;background:linear-gradient(160deg,#b3b4b1,#8d9296)" role="img" aria-label="Sensor mounted on an office wall next to a lounge area"></div>
  <div class="eyebrow" style="left:153px;top:185px">DEEP DATA INSIGHTS</div>
  <h2 class="title" style="left:153px;top:208px">Comprehensive Analytics.</h2>
  <p class="lead" style="left:153px;top:256px">Leverage high-fidelity data visualizations. Our enterprise-grade dashboard allows you to analyze historical microclimate trends with surgical precision.</p>
  <div class="chip" style="left:153px;top:290px;width:70px"><b>Cloud</b><span>NATIVE SYNC</span></div>
  <div class="chip" style="left:243px;top:290px;width:77px"><b>Vector</b><span>GRAPHICS</span></div>
  <a class="btn btn-solid" href="#" style="left:153px;top:365px;width:120px;height:26px;font-size:8.5px">Access Control Panel</a>
</section>

<section class="band band-pale feature" style="top:1885px;height:575px">
  <div class="bracket" style="left:522px;top:64px"></div>
  <div class="photo" style="left:153px;top:77px;background:linear-gradient(160deg,#bfa45c,#aaa69c)" role="img" aria-label="Sensor mounted above a doorway in a warehouse"></div>
  <div class="eyebrow" style="left:636px;top:226px">PROACTIVE PROTECTION</div>
  <h2 class="title" style="left:636px;top:248px">Automated Alerts &amp; Control.</h2>
  <p class="lead" style="left:636px;top:297px">Establish secure guardrails for your climate. Our automated notification engine triggers instantly when environmental variables exceed your defined operating parameters.</p>
  <a class="btn btn-outline" href="#" style="left:636px;top:327px;width:101px;height:26px;font-size:8.5px">Configure Alerts</a>
</section>

<footer class="site-footer">
  <nav class="footer-links">
    <a href="#">Terms of Service</a>
    <a href="#">Data Privacy</a>
    <a href="#">Cookie Policy</a>
    <a href="#">Legal Disclaimer</a>
  </nav>
  <div class="copyright">© 2026 AeroVera Infrastructure. Systematic Environmental Diagnostics.</div>
</footer>

<aside class="cookie">
  <p><strong>System Protocol:</strong> We utilize essential cookies to maintain the security and performance of our monitoring dashboard.</p>
  <a class="btn btn-solid" href="#">Authorize Session</a>
</aside>

</body>
</html>
```